Web Design Project for DJ

We need a web design for a DJ. Our client is a freelance DJ who already has a regular gig at a major night club but is looking to expand his exposure. He is located in a major metropolitan area and is looking for further gigs. He is hoping to generate further business via the website, including bookings via the site.

For reference his pagelinker page is here https://www.pagelinker.example/pages/DJ-Vorn/730162948415207

Following face to face discussions with the client today we have made a few small alterations to the brief.  We are hoping to have some images uploaded shortly.

Target Market(s)

Event planners, night club owners, radio stations, younger age groups (16-35)

Industry/Entity Type

Business

Requirements
Must have
• Name is DJVorn, this should obviously feature prominently. His current business card is attached as an example.

Links to Pagelinker and Tunedrift

Cool, modern look, slightly edgy.

Site will be built in Joomla, so a front page and secondary page template is required.
Nice to have
• Blog style layout to front page featuring recent and upcoming gigs.

Secondary pages may include a more expansive blog, a list of upcoming gigs, and a booking form.

Darker colour palettes preferred and use of same/similar fonts to those on the business card are an obvious plus

```html
<!DOCTYPE html>
<html lang="en">
<head>
<meta charset="utf-8">
<title>DJVorn — Darren Kellby</title>
<link rel="stylesheet" href="https://fonts.googleapis.com/css2?family=Raleway:wght@300;400;600&family=Open+Sans:wght@400;600;700&family=Rubik+Dirt&family=Gochi+Hand&display=swap">
<style>
  :root {
    --black: #000000;
    --ink: #111111;
    --wine: #6b0a0a;
    --wine-deep: #4a0000;
    --red-btn: #8e1212;
    --grey-light: #e4e4e4;
    --grey-mid: #a9a9a9;
    --grey-dark: #5f5f5f;
    --white: #ffffff;
    --text-soft: #d8d8d8;
  }
  * { box-sizing: border-box; margin: 0; padding: 0; }
  html, body { width: 1200px; height: 993px; overflow: hidden; background: var(--black); }
  body { position: relative; font-family: "Open Sans", sans-serif; color: var(--white); }
  .abs { position: absolute; }

  /* header */
  .nav-bar { left: 0; top: 20px; width: 1200px; height: 50px;
    background: linear-gradient(#9a9a9a, #d9d9d9 40%, #c4c4c4); }
  .brand { left: 130px; top: 0; width: 153px; height: 92px; background: var(--black); z-index: 5;
    display: flex; flex-direction: column; align-items: center; justify-content: center; padding-top: 6px; }
  .brand-name { font-family: "Raleway", sans-serif; font-weight: 600; font-size: 32px; line-height: 1; color: var(--white); }
  .brand-person { font-family: "Raleway", sans-serif; font-weight: 400; font-size: 19px; line-height: 1.1; color: var(--white); margin-top: 3px; }
  .main-nav a { position: absolute; top: 43px; font-family: "Raleway", sans-serif; font-size: 20px;
    color: var(--white); text-decoration: none; }
  .main-nav a.is-current { color: var(--wine); }

  /* photo strip */
  .photo { top: 70px; height: 207px; }
  .photo-crowd { left: 0; width: 298px; background: radial-gradient(circle at 40% 30%, #e0502a, #7a1410 55%, #200505); }
  .photo-dj { left: 300px; width: 298px; background: linear-gradient(120deg, #3a1630, #7d2f7a 40%, #1b1016 80%); }
  .photo-discoballs { left: 600px; width: 300px; background: radial-gradient(circle at 45% 40%, #d6d6d6, #6d6d6d 45%, #151515 85%); }
  .photo-lights { left: 902px; width: 298px; background: linear-gradient(135deg, #2c1fa8, #6b4fe0 40%, #16105a 75%, #05041a); }

  .tag-band { left: 0; top: 277px; width: 1200px; height: 36px;
    background: linear-gradient(#5e0000, #400000); }
  .tagline { left: 102px; top: 282px; font-family: "Gochi Hand", cursive; font-size: 19px; color: var(--white); }

  .year-tiles { left: 930px; top: 0; width: 220px; height: 370px; z-index: 6; }

  /* intro */
  .intro-title { left: 100px; top: 340px; font-family: "Rubik Dirt", sans-serif; font-size: 38px;
    font-weight: 400; color: var(--wine); line-height: 1; letter-spacing: 1px; }
  .intro-copy { left: 101px; top: 385px; width: 602px; font-size: 15.3px; line-height: 19.4px; color: var(--white); }

  /* gallery */
  .gallery { left: 775px; top: 337px; width: 323px; height: 231px; display: grid;
    grid-template-columns: 160px 161px; grid-template-rows: 114px 115px; gap: 2px; }
  .gallery div:nth-child(1) { background: linear-gradient(135deg, #8a8470, #3e3a30); }
  .gallery div:nth-child(2) { background: linear-gradient(135deg, #5c6a75, #1f262c); }
  .gallery div:nth-child(3) { background: linear-gradient(135deg, #d9d5cc, #9b3a2e); }
  .gallery div:nth-child(4) { background: linear-gradient(135deg, #d8a98a, #8a5b45); }
  .events-link { left: 776px; top: 577px; font-family: "Raleway", sans-serif; font-size: 19px; color: var(--text-soft); text-decoration: none; }
  .motto { left: 775px; top: 643px; font-family: "Rubik Dirt", sans-serif; font-size: 47px; line-height: 52px; color: #b5b5b5; white-space: nowrap; }

  /* calendar */
  .calendar { left: 100px; top: 575px; width: 258px; height: 182px;
    background: linear-gradient(#8a8a8a, #b9b9b9 60%, #9c9c9c); border: 1px solid #444; }
  .cal-head { height: 45px; background: linear-gradient(#6a6a6a, #3f3f3f 60%, #8f8f8f);
    display: flex; align-items: center; justify-content: center; gap: 14px; }
  .cal-month { font-family: "Rubik Dirt", sans-serif; font-size: 26px; color: #f0f0f0; }
  .cal-grid { position: absolute; left: 20px; top: 50px; border-collapse: collapse; font-size: 14.5px; color: var(--ink); }
  .cal-grid th { font-weight: 400; padding: 0 3px; line-height: 18px; }
  .cal-grid th.weekday { color: var(--wine); }
  .cal-grid td { text-align: center; line-height: 17.5px; padding: 0 3px; }
  .cal-grid td.past { color: var(--ink); }
  .cal-grid td.open { color: var(--white); }
  .book-btn { left: 129px; top: 742px; width: 200px; height: 31px; border-radius: 4px;
    background: linear-gradient(#b01a1a, #6e0606); font-family: "Raleway", sans-serif; font-size: 21px;
    color: var(--white); text-align: center; line-height: 31px; text-decoration: none; }

  /* social tiles */
  .social-tile { top: 633px; width: 135px; height: 124px; border: 1px solid #555;
    background: linear-gradient(#e8e8e8, #9a9a9a); text-decoration: none;
    display: flex; flex-direction: column; align-items: center; padding-top: 12px; }
  .social-tile.like { left: 393px; }
  .social-tile.share { left: 562px; }
  .social-verb { font-family: "Open Sans", sans-serif; font-weight: 700; font-size: 27px; color: var(--wine); line-height: 1.1; }
  .social-name { margin-top: 20px; display: flex; align-items: center; gap: 6px;
    font-family: "Open Sans", sans-serif; font-weight: 700; font-size: 15px; color: var(--white); }
  .social-dot { width: 12px; height: 12px; border-radius: 50%; background: var(--white); }

  /* footer */
  .site-footer { left: 0; top: 811px; width: 1200px; height: 182px; background: linear-gradient(#585858, #8c8c8c); }
  .footer-nav a { position: absolute; left: 220px; font-family: "Raleway", sans-serif; font-size: 20px; color: var(--white); text-decoration: none; }
  .divider { top: 833px; width: 0; height: 133px; border-left: 2px dotted #8e1a1a; }
  .signup { left: 499px; top: 825px; width: 204px; height: 143px; }
  .signup-card { left: 8px; top: 0; width: 188px; height: 60px; background: var(--white); border-radius: 2px; }
  .signup-input { left: 22px; top: 11px; width: 157px; height: 21px; background: var(--black);
    font-style: italic; font-size: 13px; color: var(--white); padding-left: 9px; line-height: 21px; }
  .signup-box { left: 0; top: 42px; width: 204px; height: 101px; background: linear-gradient(#f1f1f1, #8f8f8f);
    box-shadow: 0 3px 6px rgba(0,0,0,.5); text-align: center; color: var(--ink); }
  .signup-title { font-weight: 600; font-size: 21px; line-height: 22px; margin-top: 8px; }
  .signup-note { font-size: 14px; line-height: 16px; }
  .submit-btn { left: 64px; top: 113px; width: 75px; height: 23px; border-radius: 3px;
    background: linear-gradient(#b01a1a, #6e0606); color: var(--white); font-size: 17px; line-height: 23px; text-align: center; }
  .footer-social { top: 871px; font-family: "Open Sans", sans-serif; font-weight: 700; font-size: 15px; color: var(--black); text-decoration: none; }
  .footer-social.tune { color: var(--white); }
  .copyright { left: 845px; top: 948px; font-size: 11px; color: var(--white); }
</style>
</head>
<body>

<header>
  <div class="abs nav-bar"></div>
  <nav class="main-nav">
    <a class="is-current" href="#" style="left:321px">home</a>
    <a href="#" style="left:432px">events</a>
    <a href="#" style="left:560px">contact</a>
  </nav>

  <div class="abs photo photo-crowd" role="img" aria-label="Crowd with raised hands under red club lights"></div>
  <div class="abs photo photo-dj" role="img" aria-label="DJ in white shirt at the decks under purple light"></div>
  <div class="abs photo photo-discoballs" role="img" aria-label="Close-up of mirrored disco balls"></div>
  <div class="abs photo photo-lights" role="img" aria-label="Blue and violet laser lights over a dance floor"></div>

  <div class="abs brand">
    <span class="brand-name">DJVorn</span>
    <span class="brand-person">Darren Kellby</span>
  </div>

  <div class="abs tag-band"></div>
  <p class="abs tagline">I may not know everything... but I know music</p>

  <svg class="abs year-tiles" viewBox="930 0 220 370" aria-label="2013">
    <defs>
      <linearGradient id="tile" x1="0" y1="0" x2="1" y2="1">
        <stop offset="0" stop-color="#f2f2f2"/><stop offset="1" stop-color="#8d8d8d"/>
      </linearGradient>
    </defs>
    <g stroke="#9a9a9a" stroke-width="3" stroke-dasharray="3 2">
      <line x1="973" y1="8" x2="973" y2="125"/>
      <line x1="1012" y1="8" x2="1014" y2="235"/>
      <line x1="1056" y1="8" x2="1057" y2="172"/>
      <line x1="1100" y1="8" x2="1100" y2="285"/>
    </g>
    <g fill="url(#tile)" stroke="#555">
      <rect x="935" y="120" width="77" height="80"/>
      <rect x="1018" y="168" width="77" height="80"/>
      <rect x="975" y="230" width="75" height="82"/>
      <rect x="1060" y="280" width="78" height="82"/>
    </g>
    <g fill="#8e1a1a">
      <circle cx="973" cy="128" r="4"/><circle cx="1057" cy="176" r="4"/>
      <circle cx="1014" cy="238" r="4"/><circle cx="1100" cy="288" r="4"/>
    </g>
    <g font-family="Arial, sans-serif" font-weight="700" font-size="64" fill="#111" text-anchor="middle">
      <text x="974" y="195">2</text>
      <text x="1057" y="242">1</text>
      <text x="1013" y="305">0</text>
      <text x="1099" y="354">3</text>
    </g>
  </svg>
</header>

<main>
  <h1 class="abs intro-title">This is DJVorn</h1>
  <div class="abs intro-copy">
    <p>Lorem ipsum dolor sit amet, consectetur adipisicing elit, sed do eiusmod tempor incididunt ut labore et dolore magna aliqua. Ut enim ad minim veniam, quis nostrud exercitation ullamco laboris nisi ut aliquip ex ea commodo consequat. Duis aute irure dolor in reprehenderit in voluptate velit esse cillum dolore eu fugiat nulla pariatur.</p>
    <p>Lorem ipsum dolor sit amet, consectetur adipisicing elit, sed do eiusmod tempor incididunt ut labore et dolore magna aliqua. Ut enim ad minim veniam, quis nostrud exercitation ullamco laboris nisi ut aliquip ex ea commodo consequat.</p>
  </div>

  <div class="abs gallery">
    <div role="img" aria-label="Dark eye make-up with dried flowers"></div>
    <div role="img" aria-label="Group of performers posing in an alley"></div>
    <div role="img" aria-label="Young woman in plaid shirt sitting by a white wall"></div>
    <div role="img" aria-label="Close-up portrait detail"></div>
  </div>
  <a class="abs events-link" href="#">visit our events page for more &gt;&gt;</a>
  <p class="abs motto">my music<br>is my "thing"</p>

  <section class="abs calendar">
    <div class="cal-head">
      <svg width="14" height="16" viewBox="0 0 14 16"><path d="M13 1 L1 8 L13 15 Z" fill="#fff"/></svg>
      <span class="cal-month">september</span>
      <svg width="14" height="16" viewBox="0 0 14 16"><path d="M1 1 L13 8 L1 15 Z" fill="#fff"/></svg>
    </div>
    <table class="cal-grid">
      <tr><th>sun</th><th class="weekday">mon</th><th class="weekday">tue</th><th class="weekday">wed</th><th>thu</th><th class="weekday">fri</th><th class="weekday">sat</th></tr>
      <tr><td class="past">1</td><td class="open">2</td><td class="open">3</td><td class="open">4</td><td class="open">5</td><td class="open">6</td><td class="open">7</td></tr>
      <tr><td class="past">8</td><td class="open">9</td><td class="open">10</td><td class="open">11</td><td class="open">12</td><td class="open">13</td><td class="open">14</td></tr>
      <tr><td class="past">15</td><td class="open">16</td><td class="open">17</td><td class="open">18</td><td class="open">19</td><td class="open">20</td><td class="open">21</td></tr>
      <tr><td class="past">22</td><td class="past">23</td><td class="past">24</td><td class="past">25</td><td class="past">26</td><td class="past">27</td><td class="past">28</td></tr>
      <tr><td class="past">29</td><td class="past">30</td><td></td><td></td><td></td><td></td><td></td></tr>
    </table>
  </section>
  <a class="abs book-btn" href="#">Book Your Event</a>

  <a class="abs social-tile like" href="https://www.pagelinker.example/pages/DJ-Vorn/730162948415207">
    <span class="social-verb">like</span>
    <span class="social-name"><span class="social-dot"></span>Pagelinker</span>
  </a>
  <a class="abs social-tile share" href="#">
    <span class="social-verb">share</span>
    <span class="social-name"><span class="social-dot"></span>Tunedrift</span>
  </a>
</main>

<footer>
  <div class="abs site-footer"></div>
  <nav class="footer-nav">
    <a href="#" style="top:840px">home</a>
    <a href="#" style="top:874px">events</a>
    <a href="#" style="top:908px">contact</a>
  </nav>
  <div class="abs divider" style="left:386px"></div>
  <div class="abs divider" style="left:802px"></div>

  <form class="abs signup">
    <div class="abs signup-card"></div>
    <div class="abs signup-input">enter email</div>
    <div class="abs signup-box">
      <p class="signup-title">sign up</p>
      <p class="signup-note">to receive updates<br>on upcoming events</p>
    </div>
    <div class="abs submit-btn">submit</div>
  </form>

  <a class="abs footer-social" href="https://www.pagelinker.example/pages/DJ-Vorn/730162948415207" style="left:870px">Pagelinker</a>
  <a class="abs footer-social tune" href="#" style="left:966px">Tunedrift</a>
  <p class="abs copyright">Copyright © 2013 DJVORN - All Rights Reserved</p>
</footer>

</body>
</html>
```